Downloadable PDF "Brochure?"

We have a Free download we will provide in exchange for an email address on our new Trailcrest website. The website at www.venturetrailcrest-example.com is in development and will look nothing like what it currently does, but you can go there and get a sense of what Trailcrest is from the text on the website. (see the attached image 'site design' for the new redesigned website for aesthetics).

We are looking for a nice design for the document, that will represent the mostly text document well. We are not actually looking to print these at a printer so they don't have to be print ready. I went ahead and included the logo and colors and fonts file again just for reference.

Target Market(s)

Business Owners / Decision Makers

Requirements
Must have
• See attached document 'trailcrest freebie' for text to be utilized in the finished deliverable.
• See the attached image 'Site Design' for the website aesthetic.

```html
<!DOCTYPE html>
<html lang="en">
<head>
<meta charset="utf-8">
<title>Trailcrest – 10 Questions To Choose The Best Technology Advisor</title>
<link href="https://fonts.googleapis.com/css2?family=Montserrat:wght@400;500;600;700&family=Comfortaa:wght@400;600&display=swap" rel="stylesheet">
<style>
:root{
  --slate:#3a4a52;
  --copper:#c8794a;
  --ink:#4a4a4a;
  --paper:#ffffff;
  --backdrop:#e3e3e3;
  --rule:#d8d8d8;
  --photo-dark:#2b2e31;
  --photo-mid:#5d6367;
}
*{margin:0;padding:0;box-sizing:border-box}
html,body{width:713px;height:1200px;overflow:hidden}
body{background:var(--backdrop);position:relative;font-family:"Comfortaa",sans-serif;color:var(--ink)}

/* ---------- brand lockup ---------- */
.brand{position:absolute;display:flex;align-items:center;gap:6px}
.brand-mark{width:8px;height:8px;background:var(--copper);flex:none}
.brand-name{font-family:"Montserrat",sans-serif;font-weight:600;color:var(--slate);letter-spacing:.12em;line-height:1}

/* ---------- cover ---------- */
.cover{position:absolute;left:172px;top:36px;width:369px;height:520px;background:var(--paper);box-shadow:0 4px 14px rgba(0,0,0,.18);overflow:hidden}
.cover .brand{left:38px;top:62px}
.cover .brand-name{font-size:14px}
.cover-url{position:absolute;right:28px;top:64px;font-family:"Montserrat",sans-serif;font-weight:700;font-size:8px;color:var(--slate)}
.cover-art{position:absolute;left:0;top:118px}
.cover-headline{position:absolute;left:48px;top:378px;font-family:"Montserrat",sans-serif;font-weight:400;font-size:14.5px;line-height:17px;color:var(--slate);text-transform:uppercase;letter-spacing:.02em}
.cover-band{position:absolute;left:0;top:446px}
.cover-band-text{position:absolute;left:48px;top:453px;font-family:"Montserrat",sans-serif;font-size:10px;color:#fff}

/* ---------- inner pages ---------- */
.page{position:absolute;top:657px;width:322px;height:455px;background:var(--paper)}
.page-left{left:26px}
.page-right{left:366px}
.page-head{position:absolute;left:0;top:14px}
.page-title{position:absolute;left:17px;top:24px;font-family:"Montserrat",sans-serif;font-size:8px;line-height:10px;color:#fff;white-space:nowrap}
.page-title b{font-weight:700}
.page-body{position:absolute;left:17px;right:19px;top:50px;font-size:5.05px;line-height:6.6px;text-align:justify}
.page-body p{margin-bottom:7px}
.question{font-family:"Montserrat",sans-serif;font-weight:600;font-size:6px;line-height:7.6px;color:var(--copper);border-left:3px solid var(--rule);padding-left:5px;margin-left:-8px;margin-bottom:4px;text-align:left}
.answer{margin-bottom:9px}
.page-foot{position:absolute;left:0;right:0;bottom:0;height:60px}
.page-foot .brand{left:16px;top:33px;gap:4px}
.page-foot .brand-mark{width:5px;height:5px}
.page-foot .brand-name{font-size:7px}
.foot-rule{position:absolute;left:76px;right:30px;top:38px;height:1px;background:var(--slate)}
.page-num{position:absolute;right:22px;top:34px;width:9px;height:9px;border-radius:50%;background:var(--slate);color:#fff;font-family:"Montserrat",sans-serif;font-weight:700;font-size:5px;line-height:9px;text-align:center}
</style>
</head>
<body>

<section class="cover">
  <div class="brand">
    <span class="brand-mark"></span>
    <span class="brand-name">TRAILCREST</span>
  </div>
  <div class="cover-url">www.venturetrailcrest-example.com</div>

  <svg class="cover-art" width="369" height="232" viewBox="0 0 369 232">
    <defs>
      <linearGradient id="hero" x1="0" y1="0" x2="1" y2="1">
        <stop offset="0" stop-color="#3a3d40"/>
        <stop offset=".5" stop-color="var(--photo-mid)"/>
        <stop offset="1" stop-color="var(--photo-dark)"/>
      </linearGradient>
      <linearGradient id="side" x1="0" y1="0" x2="1" y2="1">
        <stop offset="0" stop-color="#3e5063"/>
        <stop offset="1" stop-color="#6d7f8e"/>
      </linearGradient>
    </defs>
    <g role="img" aria-label="Photo: businessman walking through a keyhole in a chalkboard wall of sketched business ideas toward a city skyline">
      <polygon points="0,22 308,0 270,210 0,232" fill="url(#hero)"/>
    </g>
    <polygon points="318,0 369,0 369,68 300,70" fill="var(--copper)"/>
    <g role="img" aria-label="Photo: wooden letter blocks spelling success on a desk">
      <polygon points="298,76 369,74 369,200 272,206" fill="url(#side)"/>
    </g>
  </svg>

  <h1 class="cover-headline">We help you<br>leverage technology to<br>create a competitive advantage</h1>
  <svg class="cover-band" width="369" height="26" viewBox="0 0 369 26">
    <polygon points="0,0 290,0 280,26 0,26" fill="var(--slate)"/>
  </svg>
  <div class="cover-band-text">Technology Advisors That "Get" Business</div>
</section>

<article class="page page-left">
  <svg class="page-head" width="322" height="29" viewBox="0 0 322 29">
    <rect x="0" y="0" width="8" height="29" fill="var(--copper)"/>
    <polygon points="10,0 230,0 240,29 10,29" fill="var(--slate)"/>
    <polygon points="233,0 236,0 246,29 243,29" fill="var(--copper)"/>
  </svg>
  <div class="page-title"><b>10 Questions</b> To Choose The Best Technology Advisor</div>
  <div class="page-body">
    <p>When you choose a technology advisor whether it be a Managed Service Provider, fractional CIO or a full-time CIO you need to make sure that they understand business just as much as they understand technology. Some of the biggest complaints about the IT department are that they just don't "Get it". The questions below should help you determine whether or not they have a technology mindset or a business mindset.</p>

    <div class="question">What is scalability? How important is it from a technology perspective on a scale of 1-&gt;10 with 10 being the highest? What all does scalability impact?</div>
    <p class="answer">This question is designed to get a reading on the person's mindset. A typical technology-minded response would be something describing the ability of systems or software to scale by adding additional resources. When working from a business point of view, however, you want to see it defined as the ability for the organization to support increased volume without sacrificing margins. The importance of this concept cannot be overstated and should be a 9 or 10 in terms of ranking. Regarding impact, you want to see not just an understanding of having to spend money two or three times for a different solution to the same problem, but an acknowledgment of the 'total' cost, including adoption fatigue, the opportunity cost of change, and the competitive disadvantage it creates. For concepts of business scalability refer to 'Growing Wide' by Delia Marchetti.</p>

    <div class="question">Provide an example where you solved a problem without the use of technology.</div>
    <p class="answer">Often technology-minded individuals become so wrapped up in the solutions themselves they fail to realize a policy or process change is far more effective and simple than making changes to existing or introducing new technology. Asking for a specific example here should demonstrate the ability to think from a business mindset. For specific examples reference 'The Ember Initiative' by Holt, Vance, and Pryor.</p>

    <div class="question">How do you go about prioritizing solutions in order of importance for implementation / adoption?</div>
    <p class="answer">Answers here should include reference to some form of discovery process or a thorough evaluation at the operations level. One of the key skill sets for someone approaching technology from a business point of view is mapping solutions and their respective importance to business outcomes and (often more importantly) eliminating bottlenecks while respecting that some implementations must necessarily come before others to be viable. For reference on the Theory of Constraints see '<b>The Throughline</b>' by Amos Keller.</p>

    <div class="question">What is Information Technology Debt?</div>
    <p class="answer">Stated simply, 'IT Debt' is a measurement of the out-of-date, incomplete or yet-to-be-defined technology changes. Debt occurs for a number of reasons, including lack of qualified personnel to implement the needed solutions (or recognize the problem in the first place); historical spending haunting the organization "we spent money on something like this before and look what it got us"; Fire-fighting (addressing issues purely reactively in a downward spiral leaving no time for fixing the real underlying problem); or most commonly, the budget being already allocated to other company endeavors that seem immediately more pressing. By recognizing what IT Debt is, the individual demonstrates an acknowledgment of how impactful it can be when neglected and not brought to the forefront of business planning sessions.</p>

    <div class="question">Provide an example where you argued against implementing a technology solution and why.</div>
    <p class="answer">Despite it being seemingly obvious, using 'outside of budget' is not a good answer. Business-minded technology advisors should be intimately aware of how well a proposed solution will integrate into the existing company ecosystem (software tools already present, workflow, and processes), if it drives the company toward reducing/eliminating a bottleneck (and thereby creates more leverage), and if it fits the company's culture. If any of these are a no, the solution should be carefully examined for what it really offers the organization. If yes, the budget should be evaluated as a cost-benefit analysis, not a flat number 'not to exceed'.</p>
  </div>
  <footer class="page-foot">
    <div class="brand">
      <span class="brand-mark"></span>
      <span class="brand-name">TRAILCREST</span>
    </div>
    <div class="foot-rule"></div>
    <div class="page-num">1</div>
  </footer>
</article>

<article class="page page-right">
  <svg class="page-head" width="322" height="29" viewBox="0 0 322 29">
    <rect x="0" y="0" width="8" height="29" fill="var(--copper)"/>
    <polygon points="10,0 230,0 240,29 10,29" fill="var(--slate)"/>
    <polygon points="233,0 236,0 246,29 243,29" fill="var(--copper)"/>
  </svg>
  <div class="page-title"><b>10 Questions</b> To Choose The Best Technology Advisor</div>
  <div class="page-body">
    <div class="question">What is your ideal method for maintaining technology alignment for the company?</div>
    <p class="answer">You want to see a specific process envisioned here. At the very least a recommendation to be involved in business planning meetings or retreats, and ideally a standing technology focused meeting with leadership present should be argued for. For technology to be truly in alignment, it must fit the needs of the organization, not the other way around. This needs to come from the top level, and it means a representative must be present in critical business strategy meetings to understand where the company is headed, what operational constraints they are encountering, and what their short-term goals are. For an outline of how this model has been the underlying key to success for several well-known companies reference 'Steady to Strong' by Ruth Calloway.</p>

    <div class="question">How do you plan on measuring and monitoring the adoption success of a solution or project?</div>
    <p class="answer">Technically minded individuals often look at the point of 'it's up and running and it all works', as where their responsibilities end. Someone with a business mindset should demonstrate that evaluating how well the solution has been adopted into the day to day workflow, and to what degree the solution has increased leverage or operational transparency are the true critical indicators of success. There should be a specific process of follow-up after implementation to flag adoption or workflow issues due to problems such as inadequate training, unforeseen incompatibilities (whether they be process or technology related), or simply resistance to change. These findings can then be brought back to leadership to evaluate how best to improve successful adoption going forward.</p>

    <div class="question">Provide an example where you had to balance customer and employee technology experience with security and compliance.</div>
    <p class="answer">A critical role fulfilled by a technology advisor is being able to balance maintaining compliance and sound security practices with as painless of a technology experience as possible. They should be able to weigh the critical importance of protecting the organization from the negative public relations and liability of a security flaw while respecting a solution must be usable to be useful. Look for an example that demonstrates an understanding of both sides and strikes a balance without going to an extreme in either direction.</p>

    <div class="question">What would you do first, if you were selected as our advisor? Can you give me details on what your discovery or on-boarding process includes?</div>
    <p class="answer">You are looking to make sure that they don't stop at the technology. There should be a higher focus on understanding what the company processes are and how the people inside the organization get work done. If they focus only on network, security, and disaster recovery assessments then they do not have a business mindset.</p>

    <div class="question">Can you give me an example of a time you gave a suggestion for a solution and it was not taken? Describe the solution and why it was important to the organization. And why do you think they didn't implement it?</div>
    <p class="answer">When they describe why they think the solution was important do they simply talk about risk reduction or uptime improvements without tying them back to an organizational goal or bottleneck. Being able to demonstrate actual business value is a critical skill for a technology advisor. For reference on technical excellence in service of business objectives rather than blindly servicing requirements see 'A Voice in the Room' by Owen Fairley.</p>
  </div>
  <footer class="page-foot">
    <div class="brand">
      <span class="brand-mark"></span>
      <span class="brand-name">TRAILCREST</span>
    </div>
    <div class="foot-rule"></div>
    <div class="page-num">1</div>
  </footer>
</article>

</body>
</html>
```